Re-brand our business and design!

We need a simple informational website (editable for in the future use)
We need our logo(we have included logo), name, who we are, and what we do displayed.

This is our current site (which is not acceptable, and only a template site): all our information is on this site, please use it forreferanceofinformation.
Www.brightlanefixers.com

Target Market(s)

Real estate brokers, and realtors,homeowners, and anyone looking for home repairs.

Industry/Entity Type

Business

Number of Pages Required

4 page

Font styles to use
Sans Serif

Requirements
Must have
• Our name, contact info, services, and our logo (which we will Email upon request)
• MUST have originality to the site.
• custom "contact us form" or request an estimate form.
Nice to have
• page for real customer testimonies.
• page for our previous work where we can upload pics of completed jobs.
Should not have
• any infringements on any copyrights or plagiarism at all.

```html
<!DOCTYPE html>
<html lang="en">
<head>
<meta charset="utf-8">
<title>Brightlane Home Repairs &amp; Maintenance</title>
<link rel="stylesheet" href="https://fonts.googleapis.com/css2?family=Open+Sans:ital,wght@0,400;0,600;0,700;0,800;1,400&family=Titan+One&display=swap">
<style>
:root{
  --red:#e3131b;
  --black:#111111;
  --gray:#7b7b7b;
  --card:#efefef;
  --btn:#6f6f6f;
  --text:#555555;
  --white:#ffffff;
}
*{margin:0;padding:0;box-sizing:border-box}
html,body{width:1200px;height:2990px;overflow:hidden;background:var(--white)}
body{font-family:"Open Sans",Arial,sans-serif;color:var(--text);position:relative}
.abs{position:absolute}
.top-rule{left:0;top:0;width:1200px;height:4px;background:#777}
.brand{left:76px;top:78px;color:var(--black);font-weight:800;line-height:1.15}
.brand .name{font-size:22px;display:block}
.brand .sub{font-size:13px;display:block;padding-left:80px}
.brand-mark{width:14px;height:14px;background:var(--red);display:inline-block;margin-right:8px;vertical-align:1px}
.top-contact{top:26px;font-size:15px;display:flex;align-items:center;gap:10px;color:#444}
.top-contact b{color:var(--red)}
.top-contact .email{color:var(--red);font-size:14px}
.ico-box{width:28px;height:28px;border:2px solid var(--red);border-radius:3px;display:flex;align-items:center;justify-content:center}
.nav{top:82px;left:588px;display:flex;font-size:13px;font-weight:600;color:var(--black)}
.nav a{padding:10px 22px;color:inherit;text-decoration:none}
.nav a.active{background:var(--black);color:var(--white)}
.hero{left:0;top:130px;width:1200px;height:490px;background:linear-gradient(180deg,#6d7f5e 0%,#8a6b57 45%,#6b5a4e 75%,#4e5a3a 100%)}
.hero-title{top:274px;width:1200px;text-align:center;font-family:"Titan One",Arial,sans-serif;font-size:48px;line-height:52px;color:var(--red);-webkit-text-stroke:2px var(--white)}
.hero-text{top:388px;width:1200px;text-align:center;font-size:18px;font-weight:700;line-height:26px;color:var(--white)}
.dots{top:572px;left:568px;display:flex;gap:8px}
.dots span{width:10px;height:10px;border-radius:50%;background:var(--white)}
.dots span.on{background:var(--red)}
.section-title{width:1200px;text-align:center;font-size:26px;font-weight:700;color:var(--black)}
.title-bar{width:40px;height:4px;background:var(--red);left:580px}
.card{top:752px;width:330px;height:350px;background:var(--card);text-align:center}
.card .circle{position:absolute;left:115px;top:22px;width:100px;height:100px;border:2px solid var(--red);border-radius:50%;display:flex;align-items:center;justify-content:center;background:var(--white)}
.card h3{position:absolute;top:148px;width:100%;font-size:18px;font-weight:700;color:var(--red)}
.card p{position:absolute;top:184px;left:20px;right:20px;font-size:14px;line-height:28px;color:#555}
.btn{display:inline-block;font-size:13px;font-weight:700;color:var(--white);background:var(--btn);text-align:center;line-height:44px;width:160px;height:44px}
.card .btn{position:absolute;left:85px;top:328px}
.band{left:76px;top:1176px;width:1054px;height:160px;background:linear-gradient(90deg,#2a2a2a,#1a1a1a 50%,#2a2a2a);text-align:center;color:var(--white)}
.band-arrow{left:589px;top:1162px;width:0;height:0;border-left:14px solid transparent;border-right:14px solid transparent;border-bottom:14px solid #222}
.band h2{margin-top:26px;font-size:28px;font-weight:700}
.band .serve{font-size:18px;margin-top:2px}
.band .line{margin-top:12px;font-size:18px;font-weight:700}
.band .line b{color:var(--red)}
.welcome{left:0;top:1368px;width:1200px;height:348px;background:var(--gray);color:var(--white);text-align:center}
.welcome h2{position:absolute;top:66px;width:100%;font-size:26px;font-weight:700}
.welcome p{position:absolute;top:118px;left:108px;right:108px;font-size:14px;line-height:28px}
.welcome .btn{position:absolute;left:521px;top:262px;background:var(--red);width:158px}
.gallery{left:76px;top:1860px;width:1054px;display:grid;grid-template-columns:repeat(3,1fr);gap:4px}
.gallery div{height:229px}
.g1{background:linear-gradient(160deg,#6fa4d6,#c65a3a 60%)}
.g2{background:linear-gradient(160deg,#d8d6d2,#8e8a86)}
.g3{background:linear-gradient(160deg,#b9a58c,#7a6a58)}
.g4{background:linear-gradient(160deg,#8b7a66,#3e3a36)}
.g5{background:linear-gradient(180deg,#a9c4de,#6c8a4a 50%,#8b7558)}
.g6{background:linear-gradient(160deg,#d9dbd8,#e0a640 55%,#a78a6e)}
.testimonials{left:0;top:2374px;width:1200px;height:314px;background:var(--gray);color:var(--white)}
.testimonials h2{position:absolute;top:66px;width:100%;text-align:center;font-size:26px;font-weight:700}
.avatar{left:136px;top:120px;width:132px;height:132px;border-radius:50%;border:4px solid var(--white);background:linear-gradient(160deg,#e8d6c8,#b99a80)}
.quote{left:296px;top:126px;width:760px;font-size:14px;font-style:italic;line-height:28px}
.quote .mark{font-style:normal;font-weight:800;font-size:20px}
.who{left:296px;top:228px;font-size:14px;font-weight:700}
.arrow{top:172px}
.footer{left:0;top:2688px;width:1200px;height:256px;background:var(--black);color:var(--white)}
.f-brand{left:76px;top:92px;font-weight:800;font-size:14px;line-height:1.2}
.f-brand .sub{font-size:11px;display:block;padding-left:40px}
.f-contact{left:76px;top:142px;font-size:14px;line-height:28px}
.f-contact div{display:flex;align-items:center;gap:10px}
.f-col{top:54px;font-size:14px}
.f-col h4{color:var(--red);font-size:15px;font-weight:700;margin-bottom:8px}
.f-col li{list-style:none;line-height:30px}
.socials{display:flex;gap:6px;margin-top:8px}
.socials span{width:30px;height:30px;border-radius:50%;background:#555}
.copyright{left:0;top:2944px;width:1200px;height:46px;background:var(--red);color:var(--white);text-align:center;font-size:13px;line-height:46px}
</style>
</head>
<body>
<div class="abs top-rule"></div>

<header>
  <div class="abs brand"><span class="name"><span class="brand-mark"></span>Brightlane Home Repairs</span><span class="sub">And Maintenance</span></div>
  <div class="abs top-contact" style="left:676px">
    <span class="ico-box"><svg width="14" height="14" viewBox="0 0 24 24"><path fill="#e3131b" d="M6.6 10.8a15 15 0 006.6 6.6l2.2-2.2c.3-.3.7-.4 1-.2 1.1.4 2.3.6 3.6.6.6 0 1 .4 1 1V20c0 .6-.4 1-1 1A17 17 0 013 4c0-.6.4-1 1-1h3.5c.6 0 1 .4 1 1 0 1.3.2 2.5.6 3.6.1.3 0 .7-.2 1z"/></svg></span>
    <span>Call: <b>812-555-0147</b></span>
  </div>
  <div class="abs top-contact" style="left:884px">
    <span class="ico-box"><svg width="14" height="12" viewBox="0 0 24 18"><path fill="#e3131b" d="M0 0h24v18H0z"/><path fill="none" stroke="#fff" stroke-width="2" d="M1 1l11 9 11-9"/></svg></span>
    <span class="email">dale@brightlanefixers.com</span>
  </div>
  <nav class="abs nav">
    <a class="active">HOME</a><a>ABOUT US</a><a>TESTIMONIALS</a><a>WORKS</a><a>CONTACT US</a>
  </nav>
</header>

<section>
  <div class="abs hero" role="img" aria-label="Photo of a large brick house with gabled roofs and a front porch"></div>
  <h1 class="abs hero-title">Brightlane Home Repairs<br>&amp; Maintenance</h1>
  <p class="abs hero-text">Looking for someone to help get your listing ready to show? A complete Home<br>Repair Solution? Did an inspection reveal repairs needed before closing?<br>Brightlane Home Repairs can help!</p>
  <div class="abs dots"><span class="on"></span><span></span><span></span><span></span></div>
</section>

<section>
  <div class="abs title-bar" style="top:672px"></div>
  <h2 class="abs section-title" style="top:684px">OUR SERVICES</h2>

  <div class="abs card" style="left:76px">
    <div class="circle"><svg width="50" height="50" viewBox="0 0 50 50"><g stroke="#111" stroke-width="5" stroke-linecap="round"><path d="M12 12l26 26"/><path d="M38 12L12 38"/></g><rect x="30" y="6" width="14" height="10" fill="#111" transform="rotate(45 37 11)"/></svg></div>
    <h3>CARPENTRY</h3>
    <p>Stairs, Floors, Decks, Fences<br>Storage Sheds, Storage Shelving and<br>doors Vapor Barrier Repair/Installation,<br>Attic and Crawl Space,</p>
    <span class="btn">READ MORE</span>
  </div>
  <div class="abs card" style="left:438px">
    <div class="circle"><svg width="50" height="50" viewBox="0 0 50 50"><g fill="#111"><rect x="6" y="14" width="26" height="10"/><rect x="14" y="8" width="10" height="6"/><rect x="10" y="5" width="18" height="4"/><path d="M32 14h6a4 4 0 014 4v10h-8V24h-2z"/><path d="M38 34c0 3 -2 6 0 8 2-2 0-5 0-8z"/></g></svg></div>
    <h3>PLUMBING</h3>
    <p>Bathrooms, Kitchens, Washer/Dryer Hook<br>Up Clogged drains, Toilets, Tubs/Showers<br>Sinks, Garbage disposals,<br>Leaking faucets.</p>
    <span class="btn">READ MORE</span>
  </div>
  <div class="abs card" style="left:798px;width:332px">
    <div class="circle"><svg width="50" height="50" viewBox="0 0 50 50"><g fill="#111"><rect x="8" y="8" width="34" height="34" fill="none" stroke="#111" stroke-width="3"/><path d="M10 10l10 4v26l-10-2z"/><path d="M40 10l-10 4v26l10-2z"/></g></svg></div>
    <h3>DOORS &amp; WINDOWS</h3>
    <p>Weatherstripping, Replacements<br>Glass and Screen Installation and Repair,<br>Install locksets.</p>
    <span class="btn">READ MORE</span>
  </div>
</section>

<div class="abs band-arrow"></div>
<section class="abs band">
  <h2>Home Repair Services</h2>
  <p class="serve">Serving the Maple Ridge, and surrounding areas</p>
  <p class="line">&#9990; Call: <b>812-555-0147</b> &nbsp;|&nbsp; &#9993; Email: <b>dale@brightlanefixers.com</b></p>
</section>

<section class="abs welcome">
  <div class="abs title-bar" style="top:52px"></div>
  <h2>WELCOME TO OUR WEBSITE</h2>
  <p>Aliquam molestie, mi et imperdiet euismod, dui purus auctor tellus, et interdum lacus lectus et ante. Sed accumsan sollicitudin sapien, sit amet adipiscing turpis gravida ac. In congue, neque ac lobortis volutpat, libero mauris varius mi, vitae suscipit ipsum ligula vitae risus. Duis aliquam nibh a dui iaculis viverra id a velit. Vivamus egestas risus in magna varius commodo. Sed semper viverra egestas. Etiam pretium porttitor lectus, vel ornare neque porta volutpat.</p>
  <span class="btn">READ MORE</span>
</section>

<section>
  <div class="abs title-bar" style="top:1782px"></div>
  <h2 class="abs section-title" style="top:1794px">OUR WORKS GALLERY</h2>
  <div class="abs gallery">
    <div class="g1" role="img" aria-label="Roofer working on a red tiled roof"></div>
    <div class="g2" role="img" aria-label="Plumber fixing pipes under a sink"></div>
    <div class="g3" role="img" aria-label="Carpenter fitting a door lock"></div>
    <div class="g4" role="img" aria-label="Carpenter cutting timber in a workshop"></div>
    <div class="g5" role="img" aria-label="House under construction on a building site"></div>
    <div class="g6" role="img" aria-label="Hand holding a multimeter testing wiring"></div>
  </div>
</section>

<section class="abs testimonials">
  <div class="abs title-bar" style="top:52px"></div>
  <h2>CUSTOMER TESTIMONIALS</h2>
  <svg class="abs arrow" style="left:76px" width="20" height="28" viewBox="0 0 20 28"><path d="M16 2L4 14l12 12" fill="none" stroke="#fff" stroke-width="4"/></svg>
  <svg class="abs arrow" style="left:1104px" width="20" height="28" viewBox="0 0 20 28"><path d="M4 2l12 12L4 26" fill="none" stroke="#fff" stroke-width="4"/></svg>
  <div class="abs avatar" role="img" aria-label="Customer portrait"></div>
  <p class="abs quote"><span class="mark">&ldquo;</span> Aliquam molestie, mi et imperdiet euismod, dui purus auctor tellus, et interdum lacus lectus et ante. Sed accumsan sollicitudin sapien, sit amet adipiscing turpis gravida ac. In congue, neque ac lobortis volutpat, libero mauris varius mi, vitae suscipit ipsum ligula vitae risus...<span class="mark">&rdquo;</span></p>
  <p class="abs who">-Name Heading</p>
</section>

<footer class="abs footer">
  <div class="abs f-brand">Brightlane Home Repairs<span class="sub">And Maintenance</span></div>
  <div class="abs f-contact">
    <div>&#9990; <span>Call: 812-555-0147</span></div>
    <div>&#9993; <span>Email: dale@brightlanefixers.com</span></div>
  </div>
  <div class="abs f-col" style="left:436px">
    <h4>COMPANY</h4>
    <ul><li>Home</li><li>About us</li><li>Testimonials</li><li>Works</li><li>Contact us</li></ul>
  </div>
  <div class="abs f-col" style="left:664px">
    <h4>OUR SERVICES</h4>
    <ul><li>Carpentry</li><li>Electrical</li><li>Small Construction</li><li>Plumbing</li><li>Doors &amp; Windows</li></ul>
  </div>
  <div class="abs f-col" style="left:890px">
    <h4>CONNECT US</h4>
    <div class="socials"><span></span><span></span><span></span><span></span><span></span><span></span></div>
  </div>
</footer>
<div class="abs copyright">Copyright &copy; 2016, Brightlane Home Repairs And Maintenance LLC. All rights reserved.</div>
</body>
</html>
```